Bright Harbor need a basic Calendar design

Our customers like when we give them a calendar every year but we have undergone some changes in our branding and we seek a similar product to what we delivered, but with new logos and a fresh look. If you can incorporate some stock imagery or something that is fine (like the attached apples but not necessarily that image, thats fine). This is a basic corporate calendar,

See attached photos for what we are looking for. Essentially the same exact type of wall calendar with new logo and images. That is all.

Industry/Entity Type

Product

Font styles to use
Serif
Sans Serif

Colors
3277b5
0355a3
85abd2
ffffff

```html
<!DOCTYPE html>
<html lang="en">
<head>
<meta charset="utf-8">
<title>Bright Harbor 2015 Wall Calendar</title>
<link rel="stylesheet" href="https://fonts.googleapis.com/css2?family=Arimo:wght@400;700&family=Open+Sans:wght@600;700&display=swap">
<style>
:root{
  --navy:#1b3d63;
  --brand-blue:#0355a3;
  --mid-blue:#3277b5;
  --light-blue:#85abd2;
  --white:#ffffff;
  --grey-text:#6d6e71;
  --frame:#e4e6e9;
  --rule:#c8ccd1;
  --weekend:#eef0f3;
  --hole:#bcbec0;
  --hero-light:#b9d46a;
  --hero-mid:#a3c449;
  --hero-dark:#86a834;
}
*{margin:0;padding:0;box-sizing:border-box}
html,body{width:943px;height:1200px;overflow:hidden;background:var(--white)}
body{font-family:"Arimo",Arial,sans-serif;color:var(--navy)}
.calendar{position:relative;width:943px;height:1200px;background:var(--white)}
.hanger-hole{position:absolute;top:19px;width:19px;height:16px;border-radius:50%;background:var(--hole)}
.hanger-hole.left{left:364px}
.hanger-hole.right{left:559px}
.contact{position:absolute;left:26px;top:98px}
.contact-phone{font-weight:700;font-size:35px;color:var(--light-blue);letter-spacing:-.5px;line-height:1}
.contact-web{font-weight:700;font-size:15.5px;color:var(--navy);margin-top:2px;padding-left:3px}
.year{position:absolute;left:0;right:0;top:66px;text-align:center;font-weight:700;font-size:98px;line-height:1;color:var(--navy);letter-spacing:2px}
.brand{position:absolute;right:22px;top:82px;text-align:right}
.brand-name{display:flex;align-items:center;justify-content:flex-end;gap:8px;font-family:"Open Sans",Arial,sans-serif;font-weight:600;font-size:28px;color:var(--light-blue);line-height:1}
.brand-dot{width:22px;height:22px;border-radius:50%;background:var(--mid-blue)}
.brand-division{font-weight:700;font-size:13.5px;color:var(--grey-text);margin-top:6px}
.hero{position:absolute;left:0;top:163px;width:943px;height:329px;background:linear-gradient(180deg,var(--hero-mid) 0%,var(--hero-light) 45%,var(--hero-mid) 75%,var(--hero-dark) 100%)}
.tagline{position:absolute;left:0;top:398px;width:943px;height:72px;background:rgba(255,255,255,.72);display:flex;align-items:center;justify-content:center;font-family:"Open Sans",Arial,sans-serif;font-weight:700;font-size:30.5px;color:var(--navy);letter-spacing:-.2px;white-space:nowrap}
.months{position:absolute;left:12px;top:510px;display:grid;grid-template-columns:repeat(4,226px);grid-auto-rows:195px;column-gap:5px;row-gap:28px}
.month{background:var(--frame);border-radius:8px;padding:4px 6px 6px}
.month-name{height:18px;background:var(--light-blue);border-radius:6px 6px 0 0;text-align:center;font-weight:700;font-size:15px;line-height:18px;color:var(--navy)}
.month-grid{width:100%;border-collapse:collapse;background:var(--white);table-layout:fixed}
.month-grid th{height:20px;font-size:9px;font-weight:700;color:var(--navy);text-align:center;padding-top:4px}
.month-grid td{height:29px;border:1px solid var(--rule);font-size:8.5px;text-align:right;vertical-align:top;padding:2px 3px 0 0;color:var(--navy)}
.month-grid td:first-child,.month-grid td:last-child{background:var(--weekend)}
.footer-bar{position:absolute;left:0;bottom:0;width:943px;height:15px;background:var(--light-blue)}
</style>
</head>
<body>
<div class="calendar">
  <span class="hanger-hole left"></span>
  <span class="hanger-hole right"></span>

  <header>
    <div class="contact">
      <div class="contact-phone">800 555 0142</div>
      <div class="contact-web">www.brightharborllc.com</div>
    </div>
    <h1 class="year">2015</h1>
    <div class="brand">
      <div class="brand-name"><span>bright harbor</span><span class="brand-dot"></span></div>
      <div class="brand-division">Print Solutions Division, LLC</div>
    </div>
  </header>

  <div class="hero" role="img" aria-label="Stock photo area: fresh fruit image for the calendar header"></div>
  <div class="tagline">Unique Branded Communications That Just Don’t Blend In</div>

  <main class="months">
    <section class="month"><div class="month-name">January</div>
      <table class="month-grid"><thead><tr><th>Sun</th><th>Mon</th><th>Tue</th><th>Wed</th><th>Thu</th><th>Fri</th><th>Sat</th></tr></thead><tbody>
      <tr><td></td><td></td><td></td><td></td><td>1</td><td>2</td><td>3</td></tr>
      <tr><td>4</td><td>5</td><td>6</td><td>7</td><td>8</td><td>9</td><td>10</td></tr>
      <tr><td>11</td><td>12</td><td>13</td><td>14</td><td>15</td><td>16</td><td>17</td></tr>
      <tr><td>18</td><td>19</td><td>20</td><td>21</td><td>22</td><td>23</td><td>24</td></tr>
      <tr><td>25</td><td>26</td><td>27</td><td>28</td><td>29</td><td>30</td><td>31</td></tr>
      </tbody></table></section>

    <section class="month"><div class="month-name">February</div>
      <table class="month-grid"><thead><tr><th>Sun</th><th>Mon</th><th>Tue</th><th>Wed</th><th>Thu</th><th>Fri</th><th>Sat</th></tr></thead><tbody>
      <tr><td>1</td><td>2</td><td>3</td><td>4</td><td>5</td><td>6</td><td>7</td></tr>
      <tr><td>8</td><td>9</td><td>10</td><td>11</td><td>12</td><td>13</td><td>14</td></tr>
      <tr><td>15</td><td>16</td><td>17</td><td>18</td><td>19</td><td>20</td><td>21</td></tr>
      <tr><td>22</td><td>23</td><td>24</td><td>25</td><td>26</td><td>27</td><td>28</td></tr>
      <tr><td></td><td></td><td></td><td></td><td></td><td></td><td></td></tr>
      </tbody></table></section>

    <section class="month"><div class="month-name">March</div>
      <table class="month-grid"><thead><tr><th>Sun</th><th>Mon</th><th>Tue</th><th>Wed</th><th>Thu</th><th>Fri</th><th>Sat</th></tr></thead><tbody>
      <tr><td>1</td><td>2</td><td>3</td><td>4</td><td>5</td><td>6</td><td>7</td></tr>
      <tr><td>8</td><td>9</td><td>10</td><td>11</td><td>12</td><td>13</td><td>14</td></tr>
      <tr><td>15</td><td>16</td><td>17</td><td>18</td><td>19</td><td>20</td><td>21</td></tr>
      <tr><td>22</td><td>23</td><td>24</td><td>25</td><td>26</td><td>27</td><td>28</td></tr>
      <tr><td>29</td><td>30</td><td>31</td><td></td><td></td><td></td><td></td></tr>
      </tbody></table></section>

    <section class="month"><div class="month-name">April</div>
      <table class="month-grid"><thead><tr><th>Sun</th><th>Mon</th><th>Tue</th><th>Wed</th><th>Thu</th><th>Fri</th><th>Sat</th></tr></thead><tbody>
      <tr><td></td><td></td><td></td><td>1</td><td>2</td><td>3</td><td>4</td></tr>
      <tr><td>5</td><td>6</td><td>7</td><td>8</td><td>9</td><td>10</td><td>11</td></tr>
      <tr><td>12</td><td>13</td><td>14</td><td>15</td><td>16</td><td>17</td><td>18</td></tr>
      <tr><td>19</td><td>20</td><td>21</td><td>22</td><td>23</td><td>24</td><td>25</td></tr>
      <tr><td>26</td><td>27</td><td>28</td><td>29</td><td>30</td><td></td><td></td></tr>
      </tbody></table></section>

    <section class="month"><div class="month-name">May</div>
      <table class="month-grid"><thead><tr><th>Sun</th><th>Mon</th><th>Tue</th><th>Wed</th><th>Thu</th><th>Fri</th><th>Sat</th></tr></thead><tbody>
      <tr><td>31</td><td></td><td></td><td></td><td></td><td>1</td><td>2</td></tr>
      <tr><td>3</td><td>4</td><td>5</td><td>6</td><td>7</td><td>8</td><td>9</td></tr>
      <tr><td>10</td><td>11</td><td>12</td><td>13</td><td>14</td><td>15</td><td>16</td></tr>
      <tr><td>17</td><td>18</td><td>19</td><td>20</td><td>21</td><td>22</td><td>23</td></tr>
      <tr><td>24</td><td>25</td><td>26</td><td>27</td><td>28</td><td>29</td><td>30</td></tr>
      </tbody></table></section>

    <section class="month"><div class="month-name">June</div>
      <table class="month-grid"><thead><tr><th>Sun</th><th>Mon</th><th>Tue</th><th>Wed</th><th>Thu</th><th>Fri</th><th>Sat</th></tr></thead><tbody>
      <tr><td></td><td>1</td><td>2</td><td>3</td><td>4</td><td>5</td><td>6</td></tr>
      <tr><td>7</td><td>8</td><td>9</td><td>10</td><td>11</td><td>12</td><td>13</td></tr>
      <tr><td>14</td><td>15</td><td>16</td><td>17</td><td>18</td><td>19</td><td>20</td></tr>
      <tr><td>21</td><td>22</td><td>23</td><td>24</td><td>25</td><td>26</td><td>27</td></tr>
      <tr><td>28</td><td>29</td><td>30</td><td></td><td></td><td></td><td></td></tr>
      </tbody></table></section>

    <section class="month"><div class="month-name">July</div>
      <table class="month-grid"><thead><tr><th>Sun</th><th>Mon</th><th>Tue</th><th>Wed</th><th>Thu</th><th>Fri</th><th>Sat</th></tr></thead><tbody>
      <tr><td></td><td></td><td></td><td>1</td><td>2</td><td>3</td><td>4</td></tr>
      <tr><td>5</td><td>6</td><td>7</td><td>8</td><td>9</td><td>10</td><td>11</td></tr>
      <tr><td>12</td><td>13</td><td>14</td><td>15</td><td>16</td><td>17</td><td>18</td></tr>
      <tr><td>19</td><td>20</td><td>21</td><td>22</td><td>23</td><td>24</td><td>25</td></tr>
      <tr><td>26</td><td>27</td><td>28</td><td>29</td><td>30</td><td>31</td><td></td></tr>
      </tbody></table></section>

    <section class="month"><div class="month-name">August</div>
      <table class="month-grid"><thead><tr><th>Sun</th><th>Mon</th><th>Tue</th><th>Wed</th><th>Thu</th><th>Fri</th><th>Sat</th></tr></thead><tbody>
      <tr><td>30</td><td>31</td><td></td><td></td><td></td><td></td><td>1</td></tr>
      <tr><td>2</td><td>3</td><td>4</td><td>5</td><td>6</td><td>7</td><td>8</td></tr>
      <tr><td>9</td><td>10</td><td>11</td><td>12</td><td>13</td><td>14</td><td>15</td></tr>
      <tr><td>16</td><td>17</td><td>18</td><td>19</td><td>20</td><td>21</td><td>22</td></tr>
      <tr><td>23</td><td>24</td><td>25</td><td>26</td><td>27</td><td>28</td><td>29</td></tr>
      </tbody></table></section>

    <section class="month"><div class="month-name">September</div>
      <table class="month-grid"><thead><tr><th>Sun</th><th>Mon</th><th>Tue</th><th>Wed</th><th>Thu</th><th>Fri</th><th>Sat</th></tr></thead><tbody>
      <tr><td></td><td></td><td>1</td><td>2</td><td>3</td><td>4</td><td>5</td></tr>
      <tr><td>6</td><td>7</td><td>8</td><td>9</td><td>10</td><td>11</td><td>12</td></tr>
      <tr><td>13</td><td>14</td><td>15</td><td>16</td><td>17</td><td>18</td><td>19</td></tr>
      <tr><td>20</td><td>21</td><td>22</td><td>23</td><td>24</td><td>25</td><td>26</td></tr>
      <tr><td>27</td><td>28</td><td>29</td><td>30</td><td></td><td></td><td></td></tr>
      </tbody></table></section>

    <section class="month"><div class="month-name">October</div>
      <table class="month-grid"><thead><tr><th>Sun</th><th>Mon</th><th>Tue</th><th>Wed</th><th>Thu</th><th>Fri</th><th>Sat</th></tr></thead><tbody>
      <tr><td></td><td></td><td></td><td></td><td>1</td><td>2</td><td>3</td></tr>
      <tr><td>4</td><td>5</td><td>6</td><td>7</td><td>8</td><td>9</td><td>10</td></tr>
      <tr><td>11</td><td>12</td><td>13</td><td>14</td><td>15</td><td>16</td><td>17</td></tr>
      <tr><td>18</td><td>19</td><td>20</td><td>21</td><td>22</td><td>23</td><td>24</td></tr>
      <tr><td>25</td><td>26</td><td>27</td><td>28</td><td>29</td><td>30</td><td>31</td></tr>
      </tbody></table></section>

    <section class="month"><div class="month-name">November</div>
      <table class="month-grid"><thead><tr><th>Sun</th><th>Mon</th><th>Tue</th><th>Wed</th><th>Thu</th><th>Fri</th><th>Sat</th></tr></thead><tbody>
      <tr><td>1</td><td>2</td><td>3</td><td>4</td><td>5</td><td>6</td><td>7</td></tr>
      <tr><td>8</td><td>9</td><td>10</td><td>11</td><td>12</td><td>13</td><td>14</td></tr>
      <tr><td>15</td><td>16</td><td>17</td><td>18</td><td>19</td><td>20</td><td>21</td></tr>
      <tr><td>22</td><td>23</td><td>24</td><td>25</td><td>26</td><td>27</td><td>28</td></tr>
      <tr><td>29</td><td>30</td><td></td><td></td><td></td><td></td><td></td></tr>
      </tbody></table></section>

    <section class="month"><div class="month-name">December</div>
      <table class="month-grid"><thead><tr><th>Sun</th><th>Mon</th><th>Tue</th><th>Wed</th><th>Thu</th><th>Fri</th><th>Sat</th></tr></thead><tbody>
      <tr><td></td><td></td><td>1</td><td>2</td><td>3</td><td>4</td><td>5</td></tr>
      <tr><td>6</td><td>7</td><td>8</td><td>9</td><td>10</td><td>11</td><td>12</td></tr>
      <tr><td>13</td><td>14</td><td>15</td><td>16</td><td>17</td><td>18</td><td>19</td></tr>
      <tr><td>20</td><td>21</td><td>22</td><td>23</td><td>24</td><td>25</td><td>26</td></tr>
      <tr><td>27</td><td>28</td><td>29</td><td>30</td><td>31</td><td></td><td></td></tr>
      </tbody></table></section>
  </main>

  <div class="footer-bar"></div>
</div>
</body>
</html>
```